Boys overnight camp needs a flyer in Russian Language

We're are a boys overnight camp in Ukraine. The flyer needs to portray the camp as an extreme, high intensity, fun camp with lots of exciting activities. The flyer is to promote registration. The text needed is as follows:
( Place the letters- в”н " -in the top right corner)
Лагерь “Бор Светлый Tovo”
Еврейских мальчиков
возраст 7-18 лет
30 июня -20 июля.
-увлекательные программы
-Игры, конкурсы, соревнования
-призы и подарки
походы
Пейнтбол,
Аквапарк,
Боулинг,
Каток,
Шашлыки,
Театеральные и цирковые представления,
Пляж и аттракционы
Тематически вечера у костра,
Баскетбол,
Футбол,
Волейбол,
И многое другое…
Общение с носителями англиского и иврита.
самые яркие впечатления лета 2015 в лагере бор светлый в украине!
Контакты:
050 913 7750
Больше информации: www.campotovo.example
С. ЛУГОВИЦЫ, ЖИТОМИРСКАЯ ОБЛАСТЬ
Look and feel
Each slider illustrates characteristics of the customer's brand and the style your logo design should communicate.

```html
<!DOCTYPE html>
<html lang="ru">
<head>
<meta charset="utf-8">
<title>Лагерь Бор Светлый Tovo — флаер</title>
<link rel="stylesheet" href="https://fonts.googleapis.com/css2?family=Oswald:wght@500;700&family=PT+Sans+Narrow:wght@400;700&display=swap">
<style>
  :root {
    --maroon: #8e1c1f;
    --maroon-deep: #6f1216;
    --yellow: #f7cf4a;
    --yellow-text: #f5c842;
    --teal: #7fcbbd;
    --white: #ffffff;
    --ink: #1b1b1b;
    --orange-1: #ffd24a;
    --orange-2: #f39a1c;
    --page: #ece7df;
  }
  * { box-sizing: border-box; margin: 0; padding: 0; }
  html, body { width: 993px; height: 1200px; overflow: hidden; background: var(--page); }
  .flyer {
    position: absolute; left: 76px; top: 10px;
    width: 840px; height: 1180px; overflow: hidden;
    font-family: "PT Sans Narrow", "Arial Narrow", sans-serif;
    color: var(--white);
  }
  .flyer-bg { position: absolute; inset: 0; }
  .hebrew-mark { position: absolute; right: 26px; top: 16px; font-size: 16px; font-weight: 700; }

  .brand { position: absolute; left: 26px; top: 108px; display: flex; align-items: center; gap: 12px; }
  .brand-dot { width: 40px; height: 40px; border-radius: 50%; background: var(--maroon); flex: none; }
  .brand-name {
    font-family: "Oswald", sans-serif; font-weight: 700; font-size: 24px; line-height: 1.15;
    color: var(--maroon); white-space: nowrap;
  }

  .camp-title {
    position: absolute; left: 372px; top: 70px;
    font-family: "Oswald", sans-serif; font-weight: 700; font-size: 32px; color: var(--yellow-text);
  }
  .camp-tag {
    position: absolute; left: 360px; top: 124px; width: 450px;
    background: var(--white); color: var(--ink); padding: 8px 16px;
    font-size: 22px; line-height: 1.15; box-shadow: 3px 3px 0 rgba(0,0,0,.25);
  }
  .camp-tag b { font-size: 26px; }

  .activities {
    position: absolute; left: 410px; top: 222px; list-style: none;
    font-size: 17px; line-height: 20px;
  }
  .activities li::before { content: "✓"; font-weight: 700; margin-right: 6px; }
  .activities li:nth-child(n+6) { margin-left: 22px; }
  .activities li:nth-child(n+11) { margin-left: 44px; }
  .activities li:nth-child(n+15) { margin-left: 66px; }
  .languages {
    position: absolute; left: 470px; top: 600px;
    font-size: 17px; font-weight: 700; color: var(--yellow-text);
  }

  .photo {
    position: absolute; border-radius: 50%; border: 6px solid var(--white);
    box-shadow: 0 4px 10px rgba(0,0,0,.35);
  }
  .photo-quad   { left: 30px;  top: 390px; width: 180px; height: 180px; background: linear-gradient(160deg, #8cc3e0, #b49a6b 70%); }
  .photo-banana { left: 212px; top: 362px; width: 156px; height: 156px; background: linear-gradient(180deg, #6aa7c9, #e9d53c 75%); }
  .photo-kart   { left: 40px;  top: 590px; width: 200px; height: 200px; background: linear-gradient(170deg, #5f8b4c, #4a4a4a 70%); }
  .photo-show   { left: 250px; top: 610px; width: 180px; height: 180px; background: radial-gradient(circle at 40% 40%, #e8f0ff, #7b5ab8 55%, #2b2a5a); }
  .photo-team   { left: 460px; top: 690px; width: 160px; height: 160px; background: linear-gradient(170deg, #8db3d6, #5d6b3c 60%); }

  .promo-badge {
    position: absolute; left: 657px; top: 640px; width: 160px; height: 160px; border-radius: 50%;
    background: radial-gradient(circle at 40% 35%, var(--orange-1), var(--orange-2));
    border: 4px solid var(--white);
    display: flex; align-items: center; justify-content: center; text-align: center;
    color: var(--ink); font-weight: 700; font-size: 17px; line-height: 1.1; padding: 18px;
  }

  .contacts { position: absolute; left: 50px; top: 975px; color: var(--maroon); }
  .contacts-phone { font-family: "Oswald", sans-serif; font-weight: 700; font-size: 50px; line-height: 1.1; }
  .contacts-web { font-weight: 700; font-size: 26px; margin-top: 4px; }
  .contacts-address { font-family: "Oswald", sans-serif; font-weight: 500; font-size: 30px; margin-top: 6px; }
</style>
</head>
<body>
<main class="flyer">
  <svg class="flyer-bg" viewBox="0 0 840 1180" width="840" height="1180" aria-hidden="true">
    <rect width="840" height="1180" fill="var(--maroon)"/>
    <path d="M0 0 H350 C290 150 190 320 0 420 Z" fill="var(--yellow)"/>
    <path d="M350 0 C290 150 190 320 0 420" fill="none" stroke="var(--white)" stroke-width="10"/>
    <path d="M0 960 C300 920 560 880 840 790 V1180 H0 Z" fill="var(--teal)"/>
    <path d="M0 960 C300 920 560 880 840 790" fill="none" stroke="var(--white)" stroke-width="10"/>
  </svg>

  <div class="hebrew-mark">в”н</div>

  <div class="brand">
    <span class="brand-dot"></span>
    <span class="brand-name">Бор Светлый<br>Tovo</span>
  </div>

  <h1 class="camp-title">Лагерь “Бор Светлый Tovo”</h1>
  <div class="camp-tag">
    Еврейских мальчиков<br>
    возраст <b>7-18</b> лет &nbsp;|&nbsp; <b>30</b> июня -<b>20</b> июля.
  </div>

  <ul class="activities">
    <li>увлекательные программы</li>
    <li>Игры, конкурсы, соревнования</li>
    <li>призы и подарки</li>
    <li>походы</li>
    <li>Пейнтбол,</li>
    <li>Аквапарк,</li>
    <li>Боулинг,</li>
    <li>Каток,</li>
    <li>Шашлыки,</li>
    <li>Театеральные и цирковые представления,</li>
    <li>Пляж и аттракционы</li>
    <li>Тематически вечера у костра,</li>
    <li>Баскетбол,</li>
    <li>Футбол,</li>
    <li>Волейбол,</li>
    <li>И многое другое…</li>
  </ul>
  <p class="languages">Общение с носителями англиского и иврита.</p>

  <div class="photo photo-quad" role="img" aria-label="Фото: ребята на квадроциклах у моря"></div>
  <div class="photo photo-banana" role="img" aria-label="Фото: катание на водном банане"></div>
  <div class="photo photo-kart" role="img" aria-label="Фото: картинг"></div>
  <div class="photo photo-show" role="img" aria-label="Фото: вечернее шоу с огнями"></div>
  <div class="photo photo-team" role="img" aria-label="Фото: команда после пейнтбола"></div>

  <div class="promo-badge">самые яркие впечатления лета 2015 в лагере бор светлый в украине!</div>

  <section class="contacts">
    <p class="contacts-phone">Контакты: 050 913 7750</p>
    <p class="contacts-web">Больше информации: www.campotovo.example</p>
    <p class="contacts-address">С. ЛУГОВИЦЫ, ЖИТОМИРСКАЯ ОБЛАСТЬ</p>
  </section>
</main>
</body>
</html>
```